Veteran Owned General Contractor needs Bold New Business Cards

We are a service disabled veteran owned small business. We're a general contractor that specializes in excavation, underground utilities, site work, land clearing and demolition. We would like a fresh, simple, bold, new look for our business cards. We're open to ideas! We'd like to incorporate the following information on the card:

Company Name & Logo, Name of Person, Job Title, Office Phone, Fax, Cell Phone, Email Address, Website, SDVOSB

Our logo is included. We look forward to your thoughts.

Thank you!

Reason: Hello Due to the overwhelming response to this project, we are extending the deadline one time to allow for improved communication and feedback with the top candidates. We would like to thank everyone for their hard work and exceptional creativity! Thank you

Industry/Entity Type

Business

Contact Information for Business Card

Font styles to use
Sans Serif

Requirements
Nice to have
• As we are a veteran owned company, it would be nice to incorporate an American flag into the design. Maybe on the back?

```html
<!DOCTYPE html>
<html lang="en">
<head>
<meta charset="utf-8">
<title>Ironfield Inc – Business Card</title>
<link rel="stylesheet" href="https://fonts.googleapis.com/css2?family=Montserrat:wght@400;600;700;800&display=swap">
<style>
  :root{
    --green:#6cbd45;
    --ink:#1a1a1a;
    --grey:#7a7a7a;
    --dark:#1d1d1d;
    --paper:#f7f7f7;
    --stage:#ececec;
    --white:#ffffff;
  }
  *{box-sizing:border-box;margin:0;padding:0}
  html,body{width:1200px;height:586px;overflow:hidden}
  body{background:var(--stage);font-family:'Montserrat',sans-serif;position:relative}
  .card{position:absolute;top:129px;width:502px;height:301px;overflow:hidden}
  .card--front{left:61px;background:var(--green)}
  .card--back{left:619px;background:var(--paper)}

  .veteran-badge{position:absolute;top:19px;right:0;width:102px;height:50px;background:var(--white);border-radius:8px 0 0 8px}

  .brand{position:absolute;left:0;right:0;display:flex;flex-direction:column;align-items:center}
  .brand__mark{background:var(--dark);border-radius:8px}
  .brand__name{font-weight:800;letter-spacing:1px;white-space:nowrap}
  .card--front .brand{top:88px}
  .card--front .brand__mark{width:72px;height:72px;margin-bottom:22px}
  .card--front .brand__name{color:var(--white);font-size:34px}
  .website{position:absolute;top:258px;left:0;right:0;text-align:center;font-weight:700;font-size:12px;letter-spacing:2.4px;color:var(--ink)}

  .card--back .brand{top:104px;width:257px}
  .card--back .brand__mark{width:50px;height:50px;margin-bottom:14px}
  .card--back .brand__name{color:var(--green);font-size:21px}
  .divider{position:absolute;left:257px;top:60px;width:2px;height:170px;background:linear-gradient(to bottom,transparent,var(--green),transparent)}
  .contact{position:absolute;left:286px;top:80px}
  .contact__name{color:var(--green);font-weight:600;font-size:18px}
  .contact__title{color:var(--ink);font-size:10.5px;margin-top:3px}
  .contact__list{list-style:none;margin-top:17px}
  .contact__item{display:flex;align-items:center;gap:9px;font-size:12px;color:var(--ink);height:24px}
  .contact__icon{width:17px;height:17px;flex:none}
  .address-band{position:absolute;left:0;right:0;bottom:0;height:29px;background:var(--green);display:flex;align-items:center;justify-content:center;font-weight:700;font-size:12.5px;color:var(--ink)}
</style>
</head>
<body>
  <section class="card card--front">
    <div class="veteran-badge"></div>
    <div class="brand">
      <div class="brand__mark"></div>
      <div class="brand__name">IRONFIELD INC</div>
    </div>
    <p class="website">www.ironfieldweb.com</p>
  </section>

  <section class="card card--back">
    <div class="brand">
      <div class="brand__mark"></div>
      <div class="brand__name">IRONFIELD INC</div>
    </div>
    <div class="divider"></div>
    <div class="contact">
      <h1 class="contact__name">Daniel Carter</h1>
      <p class="contact__title">Owner / Founder</p>
      <ul class="contact__list">
        <li class="contact__item">
          <svg class="contact__icon" viewBox="0 0 20 20"><circle cx="10" cy="10" r="10" fill="#6cbd45"/><path d="M6 8c0-1.5 1.8-2.5 4-2.5s4 1 4 2.5l-1.5.6-.6-1.3H8.1l-.6 1.3z M7 10h6l1 4H6z" fill="#fff"/></svg>
          503-555-0142
        </li>
        <li class="contact__item">
          <svg class="contact__icon" viewBox="0 0 20 20"><circle cx="10" cy="10" r="10" fill="#6cbd45"/><rect x="7" y="5" width="6" height="3" fill="#fff"/><rect x="5" y="8.5" width="10" height="5" rx="1" fill="#fff"/><rect x="7" y="12" width="6" height="3" fill="#fff"/></svg>
          1-800-555-0199
        </li>
        <li class="contact__item">
          <svg class="contact__icon" viewBox="0 0 20 20"><circle cx="10" cy="10" r="10" fill="#6cbd45"/><rect x="5" y="6.5" width="10" height="7" fill="#fff"/><path d="M5 6.5l5 4 5-4" fill="none" stroke="#6cbd45" stroke-width="1"/></svg>
          dan@ironfieldweb.com
        </li>
      </ul>
    </div>
    <div class="address-band">2280 Cedar Lane NE, Salem, OR 97301</div>
  </section>
</body>
</html>
```